Label for kTw Ranch beef tallow

I need a small label to go on a 2oz amber glass jar as well as a 4 oz. amber glass jar of moisturizer.
I prefer it to be rectangular for the 2oz jar since it's small and square for the 4oz jar.
I'd like to keep our kTw Ranch logo the same font and style, which is attached. Ten Sleep, Wyoming should be left out. The font for kTw Ranch is spartan.
The label content is as follows:
Meadowlark Balm
Whipped Moisturizer
Ingredients: Beef Tallow, jojoba oil, peppermint oil.
2oz. jar

Instead of a white label, I'm thinking of a tan or brown label that will blend in with the amber jar. The lettering could then be a white, cream or even rust/burgandy color. Something to give it a rich look.

Thank you!

Target Market(s)

Mainly women but men as well.

Industry/Entity Type

Ranching and online beef sales

Requirements
Must have
• kTw Ranch logo

```html
<!DOCTYPE html>
<html lang="en">
<head>
<meta charset="utf-8">
<title>kTw Ranch – Meadowlark Balm Label Versions</title>
<link rel="stylesheet" href="https://fonts.googleapis.com/css2?family=Bebas+Neue&family=Josefin+Sans:wght@300;400;600&display=swap">
<style>
  :root {
    --stage: #616161;
    --label-brown: #5a3816;
    --label-top-fade: #616161;
    --cream: #e6cfb4;
    --ivory: #f4ece2;
    --rule: #d9c3a8;
    --ribbon-text: #5a3816;
    --caption: #a3a3a3;
  }
  * { margin: 0; padding: 0; box-sizing: border-box; }
  html, body {
    width: 1200px;
    height: 1060px;
    overflow: hidden;
    background: var(--stage);
  }
  .board {
    position: relative;
    width: 1200px;
    height: 1060px;
  }
  .label {
    position: absolute;
    left: 100px;
    width: 1000px;
    height: 340px;
    color: var(--ivory);
    font-family: "Josefin Sans", sans-serif;
  }
  .label--gradient {
    top: 50px;
    background: linear-gradient(to bottom, var(--label-top-fade) 0%, var(--label-brown) 45%, var(--label-brown) 100%);
  }
  .label--solid {
    top: 560px;
    background: var(--label-brown);
  }
  .label__row {
    position: absolute;
    left: 0;
    right: 0;
    display: flex;
    justify-content: center;
    align-items: center;
  }
  .brand {
    top: 46px;
    font-size: 30px;
    font-weight: 400;
    letter-spacing: 1px;
    color: var(--ivory);
  }
  .product-name {
    top: 112px;
    font-family: "Bebas Neue", sans-serif;
    font-size: 90px;
    line-height: 1;
    letter-spacing: 1px;
    color: var(--cream);
  }
  .product-type {
    top: 190px;
    gap: 6px;
    font-size: 17px;
    font-weight: 600;
    letter-spacing: 6.5px;
    color: var(--cream);
  }
  .product-type__rule { width: 72px; height: 14px; }
  .ingredients-head {
    top: 228px;
    gap: 0;
  }
  .ingredients-head__line {
    width: 108px;
    height: 1px;
    background: var(--rule);
  }
  .ribbon {
    position: relative;
    width: 150px;
    height: 24px;
    display: flex;
    justify-content: center;
    align-items: center;
    margin: 0 4px;
  }
  .ribbon svg { position: absolute; inset: 0; }
  .ribbon__text {
    position: relative;
    font-size: 15px;
    font-weight: 600;
    color: var(--ribbon-text);
    padding-top: 3px;
  }
  .ingredients-list {
    top: 258px;
    font-size: 13px;
    font-weight: 400;
    letter-spacing: 0.6px;
  }
  .net-weight {
    top: 296px;
    font-size: 20px;
    font-weight: 400;
    color: var(--cream);
  }
  .version-caption {
    position: absolute;
    left: 0;
    right: 0;
    text-align: center;
    font-family: "Josefin Sans", sans-serif;
    font-weight: 600;
    font-size: 82px;
    color: var(--caption);
    line-height: 1;
  }
  .version-caption--one { top: 400px; }
  .version-caption--two { top: 948px; }
</style>
</head>
<body>
<main class="board">

  <section class="label label--gradient" aria-label="Label version 1">
    <div class="label__row brand">kTw Ranch</div>
    <h1 class="label__row product-name">Meadowlark Balm</h1>
    <div class="label__row product-type">
      <svg class="product-type__rule" viewBox="0 0 72 14"><g stroke="#d9c3a8" stroke-width="1"><line x1="0" y1="3.5" x2="72" y2="3.5"/><line x1="12" y1="7.5" x2="72" y2="7.5"/><line x1="0" y1="11.5" x2="72" y2="11.5"/></g></svg>
      <span>WHIPPED MOISTURIZER</span>
      <svg class="product-type__rule" viewBox="0 0 72 14"><g stroke="#d9c3a8" stroke-width="1"><line x1="0" y1="3.5" x2="72" y2="3.5"/><line x1="0" y1="7.5" x2="60" y2="7.5"/><line x1="0" y1="11.5" x2="72" y2="11.5"/></g></svg>
    </div>
    <div class="label__row ingredients-head">
      <span class="ingredients-head__line"></span>
      <div class="ribbon">
        <svg viewBox="0 0 150 24" preserveAspectRatio="none"><polygon points="0,0 150,0 142,12 150,24 0,24 8,12" fill="#f4ece2"/></svg>
        <span class="ribbon__text">INGRADIENTS</span>
      </div>
      <span class="ingredients-head__line"></span>
    </div>
    <p class="label__row ingredients-list">BEEF TALLOW, JOJOBA OIL, PEPPERMINT OIL.</p>
    <p class="label__row net-weight">2oz.</p>
  </section>
  <p class="version-caption version-caption--one">VERSION 1</p>

  <section class="label label--solid" aria-label="Label version 2">
    <div class="label__row brand">kTw Ranch</div>
    <h1 class="label__row product-name">Meadowlark Balm</h1>
    <div class="label__row product-type">
      <svg class="product-type__rule" viewBox="0 0 72 14"><g stroke="#d9c3a8" stroke-width="1"><line x1="0" y1="3.5" x2="72" y2="3.5"/><line x1="12" y1="7.5" x2="72" y2="7.5"/><line x1="0" y1="11.5" x2="72" y2="11.5"/></g></svg>
      <span>WHIPPED MOISTURIZER</span>
      <svg class="product-type__rule" viewBox="0 0 72 14"><g stroke="#d9c3a8" stroke-width="1"><line x1="0" y1="3.5" x2="72" y2="3.5"/><line x1="0" y1="7.5" x2="60" y2="7.5"/><line x1="0" y1="11.5" x2="72" y2="11.5"/></g></svg>
    </div>
    <div class="label__row ingredients-head">
      <span class="ingredients-head__line"></span>
      <div class="ribbon">
        <svg viewBox="0 0 150 24" preserveAspectRatio="none"><polygon points="0,0 150,0 142,12 150,24 0,24 8,12" fill="#f4ece2"/></svg>
        <span class="ribbon__text">INGRADIENTS</span>
      </div>
      <span class="ingredients-head__line"></span>
    </div>
    <p class="label__row ingredients-list">BEEF TALLOW, JOJOBA OIL, PEPPERMINT OIL.</p>
    <p class="label__row net-weight">2oz.</p>
  </section>
  <p class="version-caption version-caption--two">VERSION 2</p>

</main>
</body>
</html>
```